I need a business card for my original fine art pieces

I would like a business card design including a logo design for a new business in the art world. I am based in the Hunter Valley NSW Australia. I am a contemporary figurative, encaustic and wildlife artist. I would like to be able to upload my email and mobile number to this as well. This design should be one that I can incorporate into banners and flyers etc. Id like to incorporate one of my own images or partial image into the background or somewhere below. My initials are KR and I would like these used as a logo type. I would like the use of some colour and it to be bright and catchy. The final design should communicate artwork custom made and commissions available.

Overview: Original Fine Artworks for sale, online, art galleries etc, Custom made to order and by commission.

Target market is world wide audience and corporate world

My figurative work is painted using acrylics in a lot of natural ochre colours that reflect the Australian Outback, on canvas, linen, paper or board: My encaustic work is created in a contemporary abstract style using a blow torch and a made with a medium of 100% pure bees wax, Damar resin, mixed media and coloured pigments, applied to Birch board. My wildlife are created using coloured pencil and mixed media on a variety of paper types or board.

```html
<!DOCTYPE html>
<html lang="en">
<head>
<meta charset="utf-8">
<title>Kara Rowell – Business Card</title>
<link rel="stylesheet" href="https://fonts.googleapis.com/css2?family=Cinzel:wght@400&family=Open+Sans:wght@400;600;700&display=swap">
<style>
  :root {
    --backdrop: #1d1d1f;
    --card-dark: #5e5e60;
    --card-light: #ffffff;
    --accent: #e8471f;
    --ink: #1a1a1a;
    --muted: #555555;
    --faint: rgba(255,255,255,0.12);
  }
  * { margin: 0; padding: 0; box-sizing: border-box; }
  html, body { width: 1200px; height: 900px; overflow: hidden; }
  body {
    background: var(--backdrop);
    display: flex;
    flex-direction: column;
    align-items: center;
    justify-content: center;
    gap: 48px;
    font-family: "Open Sans", Arial, sans-serif;
  }
  .card {
    position: relative;
    width: 620px;
    height: 354px;
    border-radius: 26px;
    overflow: hidden;
    box-shadow: 0 14px 30px rgba(0,0,0,0.45);
  }

  /* Front */
  .card-front { background: var(--card-dark); }
  .front-ring {
    position: absolute;
    left: 50%; top: 50%;
    width: 250px; height: 250px;
    transform: translate(-50%, -50%);
    border: 5px solid var(--faint);
    border-radius: 50%;
  }
  .front-brand {
    position: absolute;
    left: 0; right: 0; top: 50%;
    transform: translateY(-50%);
    text-align: center;
    color: #fff;
  }
  .front-name {
    font-family: "Cinzel", Georgia, serif;
    font-size: 52px;
    letter-spacing: 1px;
    line-height: 1;
  }
  .front-tagline {
    margin-top: 12px;
    font-size: 21px;
    letter-spacing: 6px;
  }

  /* Back */
  .card-back { background: var(--card-light); }
  .brand-mark {
    position: absolute;
    left: 0; width: 330px; top: 0; bottom: 0;
    display: flex; align-items: center; justify-content: center;
    gap: 12px;
  }
  .brand-dot {
    width: 30px; height: 30px;
    border-radius: 50%;
    background: var(--accent);
    flex: none;
  }
  .brand-name {
    font-size: 30px;
    font-weight: 600;
    color: var(--accent);
    white-space: nowrap;
  }
  .divider {
    position: absolute;
    left: 330px; top: 70px;
    width: 1px; height: 214px;
    background: var(--ink);
  }
  .contact {
    position: absolute;
    left: 360px; top: 74px;
    color: var(--muted);
  }
  .contact-name {
    color: var(--accent);
    font-size: 27px;
    font-weight: 600;
    line-height: 1.1;
  }
  .contact-role {
    color: var(--ink);
    font-size: 15px;
    font-weight: 700;
    margin-bottom: 6px;
  }
  .contact-address { font-size: 14px; line-height: 1.4; margin-bottom: 8px; }
  .contact-list { list-style: none; font-size: 14px; }
  .contact-list li { display: flex; align-items: center; gap: 10px; line-height: 1.75; }
  .contact-list svg { width: 13px; height: 13px; fill: var(--accent); flex: none; }
  .web-highlight { color: var(--accent); }
</style>
</head>
<body>
  <section class="card card-front" aria-label="Card front">
    <div class="front-ring" aria-hidden="true"></div>
    <div class="front-brand">
      <div class="front-name">KARA ROWELL</div>
      <div class="front-tagline">ORIGINAL FINE ARTWORKS</div>
    </div>
  </section>

  <section class="card card-back" aria-label="Card back">
    <div class="brand-mark">
      <span class="brand-dot" aria-hidden="true"></span>
      <span class="brand-name">Kara Rowell</span>
    </div>
    <div class="divider"></div>
    <div class="contact">
      <div class="contact-name">Kara Rowell</div>
      <div class="contact-role">Custom Commissions</div>
      <div class="contact-address">14 Vineyard Lane<br>Pokolbin NSW 2320</div>
      <ul class="contact-list">
        <li>
          <svg viewBox="0 0 24 24" aria-hidden="true"><path d="M6.6 10.8a15.1 15.1 0 0 0 6.6 6.6l2.2-2.2a1 1 0 0 1 1-.25 11.4 11.4 0 0 0 3.6.57 1 1 0 0 1 1 1V20a1 1 0 0 1-1 1A17 17 0 0 1 3 4a1 1 0 0 1 1-1h3.5a1 1 0 0 1 1 1c0 1.25.2 2.45.57 3.6a1 1 0 0 1-.25 1z"/></svg>
          +61 400 123 456
        </li>
        <li>
          <svg viewBox="0 0 24 24" aria-hidden="true"><path d="M2 5h20v14H2z M2 5l10 8 10-8" stroke="#fff" stroke-width="1.5"/></svg>
          hello@kararowell.art
        </li>
        <li>
          <svg viewBox="0 0 24 24" aria-hidden="true"><circle cx="12" cy="12" r="10"/><path d="M2 12h20M12 2c3 3 3 17 0 20M12 2c-3 3-3 17 0 20" stroke="#fff" stroke-width="1.3" fill="none"/></svg>
          <span>www.<span class="web-highlight">kararowellart</span>.com</span>
        </li>
      </ul>
    </div>
  </section>
</body>
</html>
```